BUSINESS CARD - HALVERDINE RURAL SERVICES

I would like to create a business card for my fertilizer spreading business. I would like to incorporate my existing logo and also a description of the services offered. The business card will be given to farmers so must be kept simple but effective. It will also be left in stores so much also be eye catching in order to stand out from other cards.

Target Market(s)

FARMERS

Requirements
Must have
• FRONT OF CARD = EXISTING LOGO + "CUSTOMISED SPREADING" below the logo

REAR Of CARD = SERVICES OFFERED AND CONTACT DETAILS

- Bulk fertilizer including Lime, Gypsum, Manure & Compost
- Granular fertilizer including Single Super, Urea, Gran-am, & Custom Blends
- Modern equipment - Autosteer & Variable Rate Capable
- Friendly & Reliable Service
- Contact Gus: 0471 502 318
Nice to have
• utilize same color scheme as existing logo

```html
<!DOCTYPE html>
<html lang="en">
<head>
<meta charset="utf-8">
<title>Halverdine Rural Services – Business Card</title>
<link rel="stylesheet" href="https://fonts.googleapis.com/css2?family=Questrial&display=swap">
<style>
  :root {
    --backdrop: #e6e6e4;
    --card-white: #f7f7f6;
    --card-shade: #e4e4e3;
    --charcoal: #4a4a4c;
    --charcoal-deep: #3c3c3e;
    --orange: #e38a1c;
    --orange-deep: #c97516;
    --text-grey: #545456;
  }
  * { box-sizing: border-box; margin: 0; padding: 0; }
  html, body { width: 1200px; height: 900px; overflow: hidden; }
  body {
    background: var(--backdrop);
    font-family: "Questrial", "Century Gothic", sans-serif;
    position: relative;
  }
  .card {
    position: absolute;
    width: 680px;
    height: 390px;
    overflow: hidden;
    background: linear-gradient(120deg, var(--card-white) 40%, var(--card-shade));
    box-shadow: 0 10px 28px rgba(0,0,0,0.18);
  }
  .card-rear { left: 140px; top: 40px; }
  .card-front { left: 380px; top: 470px; }
  .card-art { position: absolute; inset: 0; width: 100%; height: 100%; }

  /* rear */
  .services {
    position: absolute;
    right: 38px;
    top: 30px;
    text-align: right;
    color: var(--text-grey);
  }
  .services-title {
    color: var(--orange);
    font-size: 21px;
    font-weight: 400;
    letter-spacing: 0.3px;
    padding-bottom: 6px;
    border-bottom: 2px solid var(--orange);
    margin-bottom: 10px;
    display: inline-block;
  }
  .services-list { list-style: none; }
  .services-list li {
    font-size: 17px;
    line-height: 30px;
  }
  .services-list li::after {
    content: "";
    display: inline-block;
    width: 7px;
    height: 7px;
    border-radius: 50%;
    background: var(--orange);
    margin-left: 12px;
    vertical-align: middle;
  }
  .contact-phone {
    margin-top: 8px;
    font-size: 21px;
    color: var(--charcoal-deep);
    letter-spacing: 1px;
    display: flex;
    justify-content: flex-end;
    align-items: center;
    gap: 10px;
  }
  .contact-phone svg { width: 22px; height: 22px; }

  /* front */
  .brand {
    position: absolute;
    left: 40px;
    top: 110px;
    width: 300px;
    display: flex;
    flex-direction: column;
    align-items: center;
    gap: 16px;
    text-align: center;
  }
  .brand-dot {
    width: 80px;
    height: 80px;
    border-radius: 50%;
    background: var(--charcoal);
    flex: none;
  }
  .brand-name {
    font-size: 32px;
    color: var(--charcoal);
    line-height: 1.15;
    letter-spacing: 0.2px;
  }
  .tagline {
    position: absolute;
    right: 58px;
    top: 40px;
    writing-mode: vertical-rl;
    color: #ffffff;
    font-size: 22px;
    letter-spacing: 3px;
  }
</style>
</head>
<body>

  <section class="card card-rear" aria-label="Back of card: services and contact">
    <svg class="card-art" viewBox="0 0 680 390">
      <circle cx="110" cy="330" r="250" fill="var(--charcoal)"/>
      <circle cx="88" cy="334" r="246" fill="#ffffff"/>
      <circle cx="80" cy="336" r="240" fill="var(--orange-deep)"/>
      <ellipse cx="100" cy="100" rx="52" ry="38" fill="var(--orange)" role="img" aria-label="Decorative orange leaf sprout on the orange disc"/>
    </svg>
    <div class="services">
      <h2 class="services-title">Services Offered And Contact Details</h2>
      <ul class="services-list">
        <li>Bulk fertilizer including Lime</li>
        <li>Gypsum, Manure &amp; Compost</li>
        <li>Granular fertilizer including Single Super</li>
        <li>Urea, Gran-am, &amp; Custom Blends</li>
        <li>Modern equipment - Autosteer</li>
        <li>&amp; Variable Rate Capable</li>
        <li>Friendly &amp; Reliable Service</li>
      </ul>
      <p class="contact-phone">0471 502 318
        <svg viewBox="0 0 24 24" aria-hidden="true">
          <path fill="var(--orange)" d="M3 8c0-2 2-4 9-4s9 2 9 4v2h-5V8H8v2H3z M6 11h12l2 9H4z"/>
          <circle cx="12" cy="15.5" r="2.4" fill="#ffffff"/>
        </svg>
      </p>
    </div>
  </section>

  <section class="card card-front" aria-label="Front of card: brand">
    <svg class="card-art" viewBox="0 0 680 390">
      <circle cx="610" cy="150" r="250" fill="var(--charcoal)"/>
      <circle cx="620" cy="140" r="236" fill="#ffffff"/>
      <circle cx="626" cy="134" r="230" fill="var(--charcoal-deep)"/>
      <path d="M400 110 C 405 60, 440 20, 500 0 L 470 0 C 430 25, 395 60, 400 110 Z" fill="var(--charcoal)" role="img" aria-label="Decorative wheat ear curving over the dark disc"/>
    </svg>
    <div class="brand">
      <span class="brand-dot" aria-hidden="true"></span>
      <span class="brand-name">Halverdine Rural<br>Services</span>
    </div>
    <p class="tagline">Customised Spreading</p>
  </section>

</body>
</html>
```